" Somos um provedor de internet que fornece principalmente o serviço de internet por fibra óptica. Também temos TV por assinatura via satélite e telefonia IP "

```html
<!DOCTYPE html>
<html lang="pt-BR">
<head>
<meta charset="UTF-8">
<title>Fibralink Internet</title>
<link rel="stylesheet" href="https://fonts.googleapis.com/css2?family=Open+Sans:wght@400;600;700&display=swap">
<style>
:root{
  --blue:#3ea8f2;
  --blue-dark:#2a93dc;
  --ink:#3a3f45;
  --muted:#8a9099;
  --line:#e4e8ec;
  --bg:#ffffff;
  --soft:#f4f6f8;
}
*{box-sizing:border-box;margin:0;padding:0}
html,body{width:1200px;height:1200px;overflow:hidden;background:var(--bg);font-family:"Open Sans",Arial,sans-serif;color:var(--ink)}
.page{position:absolute;left:300px;top:0;width:600px;height:1160px;background:#fff}
.header{position:absolute;left:0;top:0;width:600px;height:48px;display:flex;align-items:center;padding:0 36px}
.brand{display:flex;align-items:center;gap:7px;font-weight:700;font-size:13px;color:#2d4a66;letter-spacing:.5px}
.brand-mark{width:16px;height:16px;background:#2d4a66}
.nav{display:flex;gap:14px;margin-left:auto;font-size:7.5px;color:var(--ink);font-weight:600;align-items:center}
.nav svg{margin-left:6px}
.hero{position:absolute;left:0;top:48px;width:600px;height:288px;background:linear-gradient(90deg,#9eb0c0 0%,#c9d3dc 45%,#eef0f1 75%,#f6f4f2 100%)}
.hero-photo{position:absolute;inset:0}
.hero-text{position:absolute;left:43px;top:88px;width:240px;color:#fff}
.hero-title{font-size:23px;font-weight:700;line-height:1.2}
.hero-sub{font-size:7.5px;line-height:1.4;margin-top:8px;opacity:.95}
.hero-actions{display:flex;gap:8px;margin-top:18px}
.btn{display:inline-block;font-size:7px;padding:5px 12px;border-radius:2px;font-weight:600}
.btn-solid{background:var(--blue);color:#fff}
.btn-ghost{border:1px solid #fff;color:#fff}
.btn-outline-blue{border:1px solid var(--blue);color:var(--blue)}
.services{position:absolute;left:0;top:384px;width:600px;display:flex;justify-content:space-around;padding:0 60px}
.service{width:100px;text-align:center}
.service-icon{width:40px;height:40px;border-radius:50%;border:1px solid var(--line);margin:0 auto 10px;display:flex;align-items:center;justify-content:center;background:#fff}
.service-name{font-size:8.5px;font-weight:700;margin-bottom:4px}
.service-desc{font-size:6.5px;color:var(--muted);line-height:1.4}
.band{position:absolute;left:0;top:535px;width:600px;height:43px;background:var(--blue);color:#fff;font-size:11px;font-weight:600;display:flex;align-items:center;justify-content:center}
.plans-head{position:absolute;left:0;top:600px;width:600px;text-align:center}
.plans-title{font-size:16px;font-weight:400}
.plans-sub{font-size:6.5px;color:var(--muted);line-height:1.4;margin-top:3px}
.plan{position:absolute;top:670px;width:160px;text-align:center}
.plan.featured{top:650px;left:220px;height:245px;background:#fff;box-shadow:0 4px 18px rgba(0,0,0,.12);padding-top:28px}
.plan-name{font-size:9px}
.plan-speed{font-size:6px;color:var(--muted)}
.price{display:flex;justify-content:center;align-items:flex-start;margin-top:6px;font-weight:300}
.price small{font-size:7px;margin-top:9px;margin-right:2px}
.price b{font-size:40px;font-weight:400;line-height:1}
.price-period{font-size:6px;color:var(--muted);margin-top:2px}
.features{list-style:none;margin-top:12px;font-size:6.5px;color:var(--ink)}
.features li{padding:4px 0}
.plan .btn{margin-top:12px;font-size:6.5px;padding:4px 12px}
.business-photo{position:absolute;left:43px;top:940px;width:257px;height:205px;background:linear-gradient(135deg,#c9d2db 0%,#7b8a99 55%,#3e4b58 100%)}
.business-panel{position:absolute;left:300px;top:940px;width:257px;height:205px;background:var(--blue);color:#fff;padding:22px 20px}
.business-title{font-size:15px;font-weight:400;margin-bottom:10px}
.business-text{font-size:6.5px;line-height:1.5;opacity:.95}
.business-panel .btn{position:absolute;left:20px;bottom:20px;font-size:6.5px}
</style>
</head>
<body>
<div class="page">
  <header class="header">
    <div class="brand"><span class="brand-mark"></span>FIBRALINK</div>
    <nav class="nav">
      <span>Home</span><span>Contato</span><span>Internet</span><span>TV a cabo</span><span>Telefone</span><span>Assine já</span>
      <svg width="10" height="10" viewBox="0 0 10 10"><circle cx="4" cy="4" r="3" fill="none" stroke="#3a3f45" stroke-width="1.4"/><line x1="6.2" y1="6.2" x2="9" y2="9" stroke="#3a3f45" stroke-width="1.4"/></svg>
    </nav>
  </header>

  <section class="hero">
    <div class="hero-photo" role="img" aria-label="Foto de uma profissional em escritório claro com efeito de luz azul"></div>
    <div class="hero-text">
      <h1 class="hero-title">Velocidade e qualidade para a sua empresa</h1>
      <p class="hero-sub">Os melhores serviços para a sua empresa, sempre com os melhores técnicos para lhe ajudar</p>
      <div class="hero-actions"><span class="btn btn-solid">Saiba mais</span><span class="btn btn-ghost">Assine já</span></div>
    </div>
  </section>

  <section class="services">
    <div class="service">
      <div class="service-icon"><svg width="16" height="16" viewBox="0 0 16 16"><polyline points="2,12 6,7 9,10 14,4" fill="none" stroke="#3ea8f2" stroke-width="1.4"/><polyline points="11,4 14,4 14,7" fill="none" stroke="#3ea8f2" stroke-width="1.4"/></svg></div>
      <div class="service-name">Fibra Óptica</div>
      <div class="service-desc">Conexão estável e rápida direto na sua casa ou empresa.</div>
    </div>
    <div class="service">
      <div class="service-icon"><svg width="16" height="16" viewBox="0 0 16 16"><line x1="8" y1="2" x2="8" y2="10" stroke="#3ea8f2" stroke-width="1.4"/><polyline points="5,7 8,10 11,7" fill="none" stroke="#3ea8f2" stroke-width="1.4"/><polyline points="2,10 2,14 14,14 14,10" fill="none" stroke="#3ea8f2" stroke-width="1.4"/></svg></div>
      <div class="service-name">Internet Veloz</div>
      <div class="service-desc">Planos com alta velocidade de download e upload.</div>
    </div>
    <div class="service">
      <div class="service-icon"><svg width="16" height="16" viewBox="0 0 16 16"><rect x="2" y="3" width="12" height="8" fill="none" stroke="#3ea8f2" stroke-width="1.4"/><line x1="5" y1="14" x2="11" y2="14" stroke="#3ea8f2" stroke-width="1.4"/></svg></div>
      <div class="service-name">TV a Cabo</div>
      <div class="service-desc">Canais via satélite com imagem em alta definição.</div>
    </div>
    <div class="service">
      <div class="service-icon"><svg width="16" height="16" viewBox="0 0 16 16"><path d="M4 2 L6 2 L7 5 L5.5 6.5 Q7 9.5 9.5 10.5 L11 9 L14 10 L14 12 Q13 14 11 14 Q4 12 2 5 Q2 3 4 2 Z" fill="none" stroke="#3ea8f2" stroke-width="1.3"/></svg></div>
      <div class="service-name">Telefone</div>
      <div class="service-desc">Telefonia IP com ligações claras e tarifas baixas.</div>
    </div>
  </section>

  <div class="band">Serviços e atendimento de qualidade</div>

  <div class="plans-head">
    <h2 class="plans-title">Planos de Internet</h2>
    <p class="plans-sub">Escolha o plano ideal para você e navegue sem limites.<br>Instalação rápida e suporte técnico todos os dias.</p>
  </div>

  <div class="plan" style="left:52px">
    <div class="plan-name">Basic</div><div class="plan-speed">50 mega</div>
    <div class="price"><small>R$</small><b>59</b></div><div class="price-period">mês</div>
    <ul class="features"><li>Wi-fi incluso</li><li>Fibra óptica</li><li>5 mega para upload</li></ul>
    <span class="btn btn-solid">Assine já</span>
  </div>
  <div class="plan featured">
    <div class="plan-name">Medium</div><div class="plan-speed">100 mega</div>
    <div class="price"><small>R$</small><b>99</b></div><div class="price-period">mês</div>
    <ul class="features"><li>Wi-fi incluso</li><li>Fibra óptica</li><li>30 mega para upload</li></ul>
    <span class="btn btn-solid">Assine já</span>
  </div>
  <div class="plan" style="left:393px">
    <div class="plan-name">Plus</div><div class="plan-speed">200 mega</div>
    <div class="price"><small>R$</small><b>199</b></div><div class="price-period">mês</div>
    <ul class="features"><li>Wi-fi incluso</li><li>Fibra óptica</li><li>100 mega para upload</li></ul>
    <span class="btn btn-solid">Assine já</span>
  </div>

  <div class="business-photo" role="img" aria-label="Foto de executivos em reunião de negócios"></div>
  <section class="business-panel">
    <h2 class="business-title">Planos Empresariais</h2>
    <p class="business-text">Soluções completas de conectividade para empresas de todos os tamanhos. Link dedicado, IP fixo, telefonia IP e suporte prioritário com atendimento técnico especializado. Garanta mais produtividade para sua equipe com uma rede estável, segura e de alta velocidade, pensada para o seu negócio crescer.</p>
    <span class="btn btn-ghost">Saiba mais</span>
  </section>
</div>
</body>
</html>
```